Business Card Design

BBQ Concessions and Event Catering
Hi! My name is Walt I am looking for a biz card design for my BBQ company:
We specialize in ribs, brisket, pulled pork, chicken
Mainly Pork Product
Colors: Dark colors, Red, Black
Flames optional
This is a mobile trailer that moves to the party!
Copper Gate is a song by Lonnie Tasker which influenced the name of my company. So I Love Blues and BBQ!
We also cater at music venues, parties, receptions etc. Anyone who needs good BBQ comes to us.

Looking forward to your designs.

Industry/Entity Type

Business

Contact Information for Business Card

Copper Gate BBQ, Walt Barcombe Owner, 2218 Dunmore Ave. LaPorte, In. 46350

```html
<!DOCTYPE html>
<html lang="en">
<head>
<meta charset="utf-8">
<title>Copper Gate BBQ – Business Card</title>
<link rel="stylesheet" href="https://fonts.googleapis.com/css2?family=Uncial+Antiqua&family=Almendra+SC&family=Metamorphous&display=swap">
<style>
  :root {
    --ember-red: #b8262c;
    --band-red: #7a2327;
    --band-text: #2a0d0d;
    --wood-dark: #1c1410;
    --wood-mid: #4a3424;
    --ink-black: #000000;
    --paper-white: #ffffff;
  }
  * { margin: 0; padding: 0; box-sizing: border-box; }
  html, body { width: 702px; height: 1200px; overflow: hidden; background: var(--ink-black); }
  .card { position: relative; width: 702px; height: 1200px; overflow: hidden; }
  .card__top {
    position: absolute; left: 0; top: 0; width: 702px; height: 633px;
    background:
      radial-gradient(ellipse 60% 55% at 50% 55%, var(--wood-mid) 0%, rgba(60,40,28,0.6) 40%, rgba(20,14,10,0) 80%),
      repeating-linear-gradient(90deg, rgba(0,0,0,0.08) 0 2px, rgba(255,255,255,0.02) 2px 5px),
      var(--wood-dark);
  }
  .card__bottom { position: absolute; left: 0; top: 692px; width: 702px; height: 508px; background: var(--ink-black); }
  .line { position: absolute; left: 0; width: 100%; text-align: center; white-space: nowrap; }
  .brand-name {
    top: 52px; font-family: "Uncial Antiqua", serif; font-size: 66px;
    color: var(--ember-red); text-shadow: 2px 3px 3px #000;
  }
  .specialty {
    font-family: "Metamorphous", serif; font-size: 29px; letter-spacing: 1.5px;
    color: var(--ember-red); text-transform: uppercase; line-height: 48px;
  }
  .specialty--one { top: 138px; }
  .specialty--two { top: 184px; }
  .flame-art { position: absolute; left: 258px; top: 232px; width: 186px; height: 206px; }
  .mobile-note {
    font-family: "Almendra SC", serif; font-size: 48px; letter-spacing: 2px;
    color: var(--ember-red); line-height: 48px; text-shadow: 2px 2px 3px #000;
  }
  .mobile-note--one { top: 475px; }
  .mobile-note--two { top: 523px; }
  .mobile-note--three { top: 571px; }
  .service-band {
    position: absolute; left: 0; top: 633px; width: 702px; height: 59px;
    background: var(--band-red);
    font-family: "Uncial Antiqua", serif; font-size: 35px; color: var(--band-text);
    text-align: center; line-height: 59px;
  }
  .owner-name {
    top: 722px; font-family: "Uncial Antiqua", serif; font-size: 58px;
    color: var(--paper-white);
  }
  .about {
    font-family: "Almendra SC", serif; font-size: 35px; letter-spacing: 1.5px;
    color: var(--paper-white); line-height: 48px;
  }
  .about--one { top: 809px; }
  .about--two { top: 858px; }
  .about--three { top: 910px; }
  .about--four { top: 958px; }
  .address--one { top: 1064px; }
  .address--two { top: 1113px; }
</style>
</head>
<body>
<main class="card">
  <div class="card__top"></div>
  <div class="card__bottom"></div>

  <h1 class="line brand-name">Copper Gate BBQ</h1>
  <p class="line specialty specialty--one">We specialize in ribs, brisket,</p>
  <p class="line specialty specialty--two">pulled pork &amp; chicken</p>

  <svg class="flame-art" viewBox="0 0 186 206" role="img" aria-label="Red stylised flame illustration">
    <defs>
      <linearGradient id="flameTone" x1="0" y1="0" x2="0" y2="1">
        <stop offset="0" stop-color="#b8262c"/>
        <stop offset="1" stop-color="#2a0e0c"/>
      </linearGradient>
    </defs>
    <ellipse cx="93" cy="120" rx="90" ry="84" fill="url(#flameTone)" opacity="0.85"/>
  </svg>

  <p class="line mobile-note mobile-note--one">This is a mobile</p>
  <p class="line mobile-note mobile-note--two">trailer that moves</p>
  <p class="line mobile-note mobile-note--three">to the party!</p>

  <div class="service-band">BBQ &amp; CATERING</div>

  <h2 class="line owner-name">Walt Barcombe</h2>
  <p class="line about about--one">We also cater at music</p>
  <p class="line about about--two">venues, parties, receptions</p>
  <p class="line about about--three">etc. Anyone who needs good</p>
  <p class="line about about--four">BBQ comes to us!</p>
  <p class="line about address--one">2218 Dunmore Ave. LaPorte, In.</p>
  <p class="line about address--two">46350</p>
</main>
</body>
</html>
```